Byaruhanga & Odongo Advocates website

An interactive professional law firm website fully synchronized with social media pages.

Target Market(s)

Corporations and professionals

Industry/Entity Type

Professional Service

Number of Pages Required

5+ page

Font styles to use
Sans Serif

Colors

Designer to choose colors to be used in the design.

```html
<!DOCTYPE html>
<html lang="en">
<head>
<meta charset="utf-8">
<title>Byaruhanga &amp; Odongo Advocates</title>
<link rel="stylesheet" href="https://fonts.googleapis.com/css2?family=Montserrat:wght@400;500;600;700&family=Open+Sans:wght@400;600;700&display=swap">
<style>
:root{
  --red:#a61d22;
  --red-dark:#8b161a;
  --sage:#8a9e92;
  --sage-dark:#6f8478;
  --ink:#333;
  --muted:#666;
  --line:#e2e2e2;
  --grey-band:#ececec;
  --footer:#2a2a2a;
  --footer-text:#a9a9a9;
  --gold:#d3a95b;
  --white:#fff;
}
*{box-sizing:border-box;margin:0;padding:0}
html,body{width:1200px;height:3523px;overflow:hidden}
body{font-family:"Open Sans",Arial,sans-serif;color:var(--ink);background:var(--white);font-size:11px;line-height:1.7}
h1,h2,h3,h4{font-family:"Montserrat",Arial,sans-serif}
.wrap{width:880px;margin:0 auto;position:relative}
section,header,footer{position:relative}

/* top bar */
.topbar{height:28px;background:var(--red-dark);color:#f3dede;font-size:10px}
.topbar .wrap{display:flex;align-items:center;height:28px}
.topbar .contact{display:flex;gap:22px}
.topbar .contact span{display:flex;align-items:center;gap:6px}
.topbar .social{margin-left:auto;display:flex;gap:14px;align-items:center}
.dot{width:9px;height:9px;border-radius:50%;background:#f1d5d5;display:block}
.topbar .appoint{margin-left:18px;background:#fff;color:var(--red);padding:2px 10px;font-size:9px;border-radius:2px}

/* header */
.site-header{height:62px;background:#fff;border-bottom:1px solid var(--line)}
.site-header .wrap{display:flex;align-items:center;height:62px}
.brand{display:flex;align-items:center;gap:10px}
.brand-mark{width:34px;height:34px;background:var(--red)}
.brand-name{font-family:"Montserrat",sans-serif;font-weight:600;color:var(--red);font-size:13px;line-height:1.2}
.brand-name small{display:block;font-size:8px;color:#999;font-weight:500;letter-spacing:1px}
.nav{margin-left:auto;display:flex;gap:4px;font-family:"Montserrat",sans-serif;font-size:10px;font-weight:600}
.nav a{color:#333;text-decoration:none;padding:6px 10px}
.nav a.active{background:var(--red);color:#fff}

/* hero */
.hero{height:525px;background:linear-gradient(180deg,#3c3a3a 0%,#2c2726 55%,#1b1817 100%);color:#fff;text-align:center}
.hero-photo{position:absolute;inset:0;background:radial-gradient(ellipse at 50% 40%,rgba(120,110,100,.35),rgba(0,0,0,0) 65%)}
.hero h1{position:absolute;top:200px;left:0;right:0;font-size:46px;font-weight:600;letter-spacing:1px}
.hero .tagline{position:absolute;top:272px;left:0;right:0;font-family:"Montserrat",sans-serif;font-size:13px;letter-spacing:4px}
.btn{display:inline-block;background:var(--red);color:#fff;font-family:"Montserrat",sans-serif;font-size:10px;font-weight:600;letter-spacing:1px;text-decoration:none}
.hero .btn{position:absolute;top:322px;left:535px;width:130px;height:36px;line-height:36px}
.slide-arrow{position:absolute;top:332px;width:22px;height:40px;background:rgba(255,255,255,.15);display:flex;align-items:center;justify-content:center}
.slide-arrow.prev{left:0}.slide-arrow.next{right:0}

/* values + history */
.intro{height:648px}
.values{position:absolute;top:-33px;left:160px;width:880px;height:240px;background:var(--red);display:flex;color:#fff;text-align:center}
.value{flex:1;padding:22px 34px 0}
.value-icon{width:56px;height:56px;margin:0 auto 6px;border:2px solid #fff;border-radius:50%;display:flex;align-items:center;justify-content:center}
.value h3{font-size:17px;font-weight:700;margin-bottom:8px}
.value p{font-size:10.5px;line-height:1.65;color:#f6e2e2}
.section-head{text-align:center}
.section-head svg{display:block;margin:0 auto 10px}
.section-head h2{font-size:21px;font-weight:700;color:#222;letter-spacing:.5px}
.intro .section-head{position:absolute;top:240px;left:0;right:0}
.history{position:absolute;top:336px;left:160px;width:880px;display:flex;gap:24px}
.history-photo{width:427px;height:263px;flex:none;background:linear-gradient(135deg,#4d2a26,#8a6a58 50%,#3b2d2a)}
.history-text p{font-size:10.5px;color:var(--muted);margin-bottom:14px;line-height:1.75}

/* who we are */
.who{height:451px;background:var(--sage);color:#fff;text-align:center}
.who .section-head{padding-top:60px}
.who .section-head h2{color:#fff}
.who .lead{width:640px;margin:14px auto 0;font-size:11px;line-height:1.7;color:#f1f4f2}
.pillars{display:flex;justify-content:center;gap:60px;margin-top:34px}
.pillar{width:300px}
.pillar-icon{width:82px;height:82px;border-radius:50%;background:#fff;margin:0 auto 12px;display:flex;align-items:center;justify-content:center}
.pillar h3{font-size:21px;font-weight:600;margin-bottom:4px}
.pillar p{font-size:11px;line-height:1.6;color:#f1f4f2}

/* stats */
.stats{height:207px;background:linear-gradient(90deg,#2a1a12,#4a3220 40%,#3a2718 70%,#1d130d)}
.stats .row{position:absolute;top:70px;left:180px;right:150px;display:flex;justify-content:space-between}
.stat{display:flex;align-items:flex-start;gap:14px;color:#fff}
.stat-num{border-left:1px solid rgba(255,255,255,.5);padding-left:8px}
.stat-num b{display:block;font-family:"Montserrat",sans-serif;font-size:42px;font-weight:600;line-height:1}
.stat-num span{display:block;font-size:10.5px;line-height:1.3;margin-top:4px;width:110px}

/* practice areas */
.practice{height:392px}
.practice .section-head{padding-top:60px}
.cards{position:absolute;top:145px;left:160px;width:880px;display:flex;gap:16px}
.card{flex:1;height:195px;border:1px solid var(--line);text-align:center;padding:28px 24px 0}
.card h3{color:var(--red);font-size:12px;font-weight:700;margin:8px 0 6px}
.card p{font-size:10.5px;color:var(--muted);line-height:1.65}
.card .more{display:block;margin-top:6px;font-size:10px;color:#888}

/* clients */
.clients{height:364px;background:var(--grey-band)}
.clients .section-head{padding-top:56px}
.tabs{position:absolute;top:129px;left:270px;display:flex;font-family:"Montserrat",sans-serif;font-size:9.5px;font-weight:700;color:#fff}
.tab{height:38px;line-height:38px;text-align:center}
.tab.t1{width:277px;background:var(--red)}
.tab.t2{width:209px;background:var(--sage)}
.tab.t3{width:174px;background:var(--sage-dark)}
.logos{position:absolute;top:206px;left:204px;display:flex;gap:28px}
.logo{width:75px;height:75px;background:#fff;border-radius:8px;display:flex;align-items:center;justify-content:center;font-family:"Montserrat",sans-serif;font-weight:700;font-size:12px;color:#444}
.pager{position:absolute;top:310px;left:0;right:0;display:flex;justify-content:center;gap:6px}
.pager i{width:8px;height:8px;border-radius:50%;background:#bbb}
.pager i.on{background:var(--red)}

/* team */
.team{height:375px}
.team .section-head{padding-top:48px}
.people{position:absolute;top:150px;left:160px;display:flex;gap:23px}
.person{width:128px;text-align:center}
.portrait{height:122px;background:linear-gradient(180deg,#6f6860,#3f3a35)}
.person h4{color:var(--red);font-size:9.5px;font-weight:700;margin-top:10px;line-height:1.2}
.person p{font-size:8.5px;color:#666;line-height:1.3}
.team-arrow{position:absolute;top:196px;width:26px;height:32px;border:1px solid #ccc;display:flex;align-items:center;justify-content:center}
.team-arrow.prev{left:104px}.team-arrow.next{left:1068px}

/* footer */
.site-footer{height:471px;background:var(--footer);color:var(--footer-text)}
.newsletter{position:absolute;top:45px;left:160px;width:880px;height:50px;display:flex;align-items:center}
.newsletter h3{color:var(--gold);font-size:20px;font-weight:500;width:290px}
.newsletter .field{flex:1;height:30px;border-bottom:1px solid #555;font-size:10px;color:#888;line-height:30px;padding-left:4px;position:relative}
.newsletter .btn{position:absolute;right:0;top:0;width:114px;height:30px;line-height:30px;text-align:center;border-radius:15px}
.footer-cols{position:absolute;top:110px;left:160px;width:880px;display:flex;border-top:1px solid #3a3a3a;padding-top:22px}
.footer-cols h4{color:#fff;font-size:12px;font-weight:700;margin-bottom:22px}
.col-about{width:343px}
.col-about p{font-size:10.5px;line-height:1.75;width:280px}
.col-links{width:169px}.col-services{width:180px}
.col-contact{width:188px}
.footer-cols ul{list-style:none}
.footer-cols li{font-size:10.5px;margin-bottom:17px}
.footer-cols li::before{content:"›";margin-right:8px}
.col-contact p{font-size:10px;line-height:1.55;margin-bottom:10px;display:flex;gap:8px}
.col-contact strong{color:#ddd}
.footer-social{display:flex;gap:16px;margin-top:20px}
.footer-social .dot{background:#999}
.copyright{position:absolute;top:433px;left:160px;width:880px;border-top:1px solid #3a3a3a;text-align:center;font-size:9.5px;padding-top:12px;color:#888}
</style>
</head>
<body>

<div class="topbar">
  <div class="wrap">
    <div class="contact">
      <span><svg width="9" height="9" viewBox="0 0 10 10"><path d="M2 1l2 2-1 1.5c.6 1.2 1.3 1.9 2.5 2.5L7 6l2 2-1.5 1.5C4.5 9 1 5.5.5 2.5z" fill="#f3dede"/></svg>Call us: +256 (0) 700 123 456</span>
      <span><svg width="10" height="8" viewBox="0 0 10 8"><rect x=".5" y=".5" width="9" height="7" fill="none" stroke="#f3dede"/><path d="M.5.5l4.5 4 4.5-4" fill="none" stroke="#f3dede"/></svg>advocates@byodlaw.com</span>
    </div>
    <div class="social">
      <i class="dot" aria-label="Social page"></i><i class="dot" aria-label="Social page"></i><i class="dot" aria-label="Social page"></i><i class="dot" aria-label="Social page"></i>
      <span class="appoint">Make An Appointment</span>
    </div>
  </div>
</div>

<header class="site-header">
  <div class="wrap">
    <div class="brand">
      <span class="brand-mark"></span>
      <div class="brand-name">Byaruhanga &amp; Odongo<small>ADVOCATES</small></div>
    </div>
    <nav class="nav">
      <a class="active" href="#">HOME</a><a href="#">ABOUT</a><a href="#">PRACTICE AREA</a><a href="#">CASES</a><a href="#">NEWS</a><a href="#">CONTACT</a>
    </nav>
  </div>
</header>

<section class="hero">
  <div class="hero-photo" role="img" aria-label="Group photo of the firm's advocates in dark suits"></div>
  <h1>WE ARE VOICE OF JUSTICE</h1>
  <p class="tagline">CONSTRUCTION LAW &nbsp;|&nbsp; ARBITRATION &nbsp;|&nbsp; LITIGATION</p>
  <a class="btn" href="#">CONTACT US</a>
  <span class="slide-arrow prev"><svg width="8" height="12" viewBox="0 0 8 12"><path d="M6 1L1 6l5 5" stroke="#fff" stroke-width="2" fill="none"/></svg></span>
  <span class="slide-arrow next"><svg width="8" height="12" viewBox="0 0 8 12"><path d="M2 1l5 5-5 5" stroke="#fff" stroke-width="2" fill="none"/></svg></span>
</section>

<section class="intro">
  <div class="values">
    <div class="value">
      <div class="value-icon"><svg width="28" height="24" viewBox="0 0 28 24" fill="none" stroke="#fff" stroke-width="2"><path d="M14 2v20M6 22h16M4 5h20M4 5l-3 8h6zM24 5l-3 8h6z"/></svg></div>
      <h3>Integrity</h3>
      <p>We maintain ethical behaviour and strict moral values. We are honest and trustworthy in our dealings with each other, with our clients and with all others with whom we deal.</p>
    </div>
    <div class="value">
      <div class="value-icon"><svg width="28" height="20" viewBox="0 0 28 20" fill="none" stroke="#fff" stroke-width="2"><path d="M1 8l7-6 6 4 6-4 7 6-9 9-4-3-4 3z"/></svg></div>
      <h3>Partnership</h3>
      <p>We partner with our clients and keep a close and interactive relationship that enriches our business knowledge and allows us to provide strategic, innovative and forward-thinking solutions fit to meet the challenges they face every day.</p>
    </div>
    <div class="value">
      <div class="value-icon"><svg width="22" height="28" viewBox="0 0 22 28" fill="none" stroke="#fff" stroke-width="2"><circle cx="11" cy="10" r="8"/><path d="M7 21h8M8 25h6"/></svg></div>
      <h3>Efficiency</h3>
      <p>We work to surpass our clients' expectations. We are practical and solution driven in our approach. We are innovative and creative, and we focus sharply and firmly on the issues we undertake.</p>
    </div>
  </div>

  <div class="section-head">
    <svg width="26" height="22" viewBox="0 0 26 22"><rect x="6" y="2" width="12" height="6" transform="rotate(-35 12 5)" fill="#a61d22"/><rect x="12" y="8" width="3" height="11" transform="rotate(-35 13 13)" fill="#a61d22"/><rect x="2" y="19" width="12" height="2" fill="#a61d22"/></svg>
    <h2>OUR HISTORY</h2>
  </div>

  <div class="history">
    <div class="history-photo" role="img" aria-label="Team photo of partners and associates at the office"></div>
    <div class="history-text">
      <p>In 1996, our firm was founded and is comprised of 5 Partners and over 15 Associates and support staff fully engaged and focused on client service. The firm is fully automated and is run on the latest practice management software with efficient client focused delivery systems and improved turn around times.</p>
      <p>Over the years, the firm has worked with the international firm of Harrow Whitfield in successfully representing Civic Rights Trust against a multimillion dollar law suit and has acted for both local and international corporations from China, Italy, Turkey, South Africa, Zambia and the United Kingdom to build their businesses.</p>
      <p>With over 21 years' experience and having achieved tremendous success for our clients having won over 200 commercial disputes, we are now a specialist firm in Commercial Litigation, Construction Law and Arbitration. We have successfully represented clients in ground breaking cases in the financial services sector that we are the firm of choice in banking and insurance litigation.</p>
    </div>
  </div>
</section>

<section class="who">
  <div class="section-head">
    <svg width="26" height="22" viewBox="0 0 26 22"><rect x="6" y="2" width="12" height="6" transform="rotate(-35 12 5)" fill="#fff"/><rect x="12" y="8" width="3" height="11" transform="rotate(-35 13 13)" fill="#fff"/><rect x="2" y="19" width="12" height="2" fill="#fff"/></svg>
    <h2>WHO WE ARE</h2>
  </div>
  <p class="lead">Byaruhanga &amp; Odongo Advocates are a specialist commercial law firm in Uganda focusing on commercial litigation, construction law and arbitration. We have excelled in our niche areas for over two decades and we continue to grow and be the firm choice in those practice areas.</p>
  <div class="pillars">
    <div class="pillar">
      <div class="pillar-icon"><svg width="44" height="28" viewBox="0 0 44 28"><path d="M2 14C10 3 34 3 42 14 34 25 10 25 2 14z" fill="#8a9e92"/><circle cx="22" cy="14" r="7" fill="#fff"/><circle cx="22" cy="14" r="4" fill="#8a9e92"/></svg></div>
      <h3>Vision</h3>
      <p>To be the firm of choice in our niche practice<br>areas of commercial law.</p>
    </div>
    <div class="pillar">
      <div class="pillar-icon"><svg width="40" height="36" viewBox="0 0 40 36"><path d="M2 17L38 2 30 34 20 24z" fill="#8a9e92"/><path d="M20 24l18-22-22 20z" fill="#fff" opacity=".6"/></svg></div>
      <h3>Mission</h3>
      <p>To provide legal services focused on commercial litigation, construction law and arbitration with efficiency, integrity and client satisfaction.</p>
    </div>
  </div>
</section>

<section class="stats" role="img" aria-label="Dark wooden desk with a judge's gavel">
  <div class="row">
    <div class="stat">
      <svg width="44" height="30" viewBox="0 0 44 30" fill="#d3a95b"><circle cx="22" cy="8" r="6"/><circle cx="9" cy="11" r="5"/><circle cx="35" cy="11" r="5"/><path d="M12 30c0-10 20-10 20 0zM1 30c0-8 14-9 14-3v3zM43 30c0-8-14-9-14-3v3z"/></svg>
      <div class="stat-num"><b>5</b><span>Partners</span></div>
    </div>
    <div class="stat">
      <svg width="40" height="30" viewBox="0 0 40 30" fill="#d3a95b"><circle cx="20" cy="7" r="6"/><circle cx="8" cy="12" r="5"/><circle cx="32" cy="12" r="5"/><path d="M10 30c0-12 20-12 20 0zM0 30c0-9 14-9 14-2v2zM40 30c0-9-14-9-14-2v2z"/></svg>
      <div class="stat-num"><b>20+</b><span>People</span></div>
    </div>
    <div class="stat">
      <svg width="38" height="34" viewBox="0 0 38 34" fill="#d3a95b"><rect x="10" y="3" width="18" height="9" transform="rotate(-35 19 7)"/><rect x="18" y="12" width="4" height="16" transform="rotate(-35 20 20)"/><rect x="2" y="30" width="18" height="4"/></svg>
      <div class="stat-num"><b>55</b><span>Years of Combined Experience</span></div>
    </div>
    <div class="stat">
      <svg width="38" height="32" viewBox="0 0 38 32" fill="#d3a95b"><rect x="2" y="8" width="34" height="22" rx="2"/><rect x="13" y="2" width="12" height="7" fill="none" stroke="#d3a95b" stroke-width="3"/></svg>
      <div class="stat-num"><b>350+</b><span>Cases Solved</span></div>
    </div>
  </div>
</section>

<section class="practice">
  <div class="section-head">
    <svg width="26" height="22" viewBox="0 0 26 22"><rect x="6" y="2" width="12" height="6" transform="rotate(-35 12 5)" fill="#a61d22"/><rect x="12" y="8" width="3" height="11" transform="rotate(-35 13 13)" fill="#a61d22"/><rect x="2" y="19" width="12" height="2" fill="#a61d22"/></svg>
    <h2>PRACTICE AREAS</h2>
  </div>
  <div class="cards">
    <div class="card">
      <svg width="30" height="26" viewBox="0 0 30 26" fill="#a61d22"><path d="M15 0L0 8h30z"/><rect x="3" y="10" width="4" height="11"/><rect x="13" y="10" width="4" height="11"/><rect x="23" y="10" width="4" height="11"/><rect x="0" y="22" width="30" height="4"/></svg>
      <h3>CONSTRUCTION LAW</h3>
      <p>Our Construction Law department is headed by our Senior Partner Martin Odongo, who is highly qualified and experienced in Construction law</p>
      <span class="more">Read More →</span>
    </div>
    <div class="card">
      <svg width="30" height="26" viewBox="0 0 30 26" fill="#a61d22"><rect x="0" y="6" width="30" height="20"/><rect x="3" y="0" width="4" height="6"/><rect x="13" y="0" width="4" height="6"/><rect x="23" y="0" width="4" height="6"/><rect x="4" y="11" width="4" height="4" fill="#fff"/><rect x="13" y="11" width="4" height="4" fill="#fff"/><rect x="22" y="11" width="4" height="4" fill="#fff"/></svg>
      <h3>COMMERCIAL LITIGATION</h3>
      <p>We have a reputation for producing excellent results for our litigation clients. Since 1996, the firm has an excellent track</p>
      <span class="more">Read More →</span>
    </div>
    <div class="card">
      <svg width="30" height="26" viewBox="0 0 30 26" fill="#a61d22"><rect x="10" y="2" width="14" height="7" transform="rotate(-35 17 5)"/><rect x="14" y="9" width="3" height="13" transform="rotate(-35 15 15)"/><rect x="1" y="22" width="16" height="4"/></svg>
      <h3>ARBITRATION</h3>
      <p>We advise clients on both domestic and international arbitration proceedings and other forms of intermediate and alternative dispute resolution</p>
      <span class="more">Read More →</span>
    </div>
  </div>
</section>

<section class="clients">
  <div class="section-head">
    <svg width="26" height="22" viewBox="0 0 26 22"><rect x="6" y="2" width="12" height="6" transform="rotate(-35 12 5)" fill="#a61d22"/><rect x="12" y="8" width="3" height="11" transform="rotate(-35 13 13)" fill="#a61d22"/><rect x="2" y="19" width="12" height="2" fill="#a61d22"/></svg>
    <h2>OUR CLIENTS</h2>
  </div>
  <div class="tabs">
    <div class="tab t1">COMMERCIAL LITIGATION &amp; TRANSACTIONS</div>
    <div class="tab t2">CONSTRUCTION &amp; ARBITRATION</div>
    <div class="tab t3">CORPORATE ADVISORY</div>
  </div>
  <div class="logos">
    <div class="logo">Kiwa</div><div class="logo">Norda</div><div class="logo">Plexa</div><div class="logo">Tembo</div><div class="logo">Rivo</div><div class="logo">Umoja</div><div class="logo">Savanna</div><div class="logo">Lakeline</div>
  </div>
  <div class="pager"><i class="on"></i><i></i></div>
</section>

<section class="team">
  <div class="section-head">
    <svg width="26" height="22" viewBox="0 0 26 22"><rect x="6" y="2" width="12" height="6" transform="rotate(-35 12 5)" fill="#a61d22"/><rect x="12" y="8" width="3" height="11" transform="rotate(-35 13 13)" fill="#a61d22"/><rect x="2" y="19" width="12" height="2" fill="#a61d22"/></svg>
    <h2>OUR PROFESSIONALS</h2>
  </div>
  <span class="team-arrow prev"><svg width="7" height="11" viewBox="0 0 7 11"><path d="M6 1L1 5.5 6 10" stroke="#777" stroke-width="1.5" fill="none"/></svg></span>
  <div class="people">
    <div class="person"><div class="portrait" role="img" aria-label="Portrait of the managing partner"></div><h4>PETER A. BYARUHANGA</h4><p>Managing Partner</p></div>
    <div class="person"><div class="portrait" role="img" aria-label="Portrait of the senior partner"></div><h4>MARTIN J. ODONGO</h4><p>Senior Partner</p></div>
    <div class="person"><div class="portrait" role="img" aria-label="Portrait of the head of litigation"></div><h4>SAMUEL OKELLO</h4><p>Partner<br>(Head of Litigation)</p></div>
    <div class="person"><div class="portrait" role="img" aria-label="Portrait of the head of business development"></div><h4>NATHAN MUGISHA</h4><p>Partner<br>(Head of Business Development)</p></div>
    <div class="person"><div class="portrait" role="img" aria-label="Portrait of the head of corporate advisory"></div><h4>GRACE NAMUTEBI</h4><p>Partner<br>(Head of Corporate Advisory)</p></div>
    <div class="person"><div class="portrait" role="img" aria-label="Portrait of the senior legal associate"></div><h4>ALEX KIWANUKA</h4><p>Senior Legal Associate</p></div>
  </div>
  <span class="team-arrow next"><svg width="7" height="11" viewBox="0 0 7 11"><path d="M1 1l5 4.5L1 10" stroke="#777" stroke-width="1.5" fill="none"/></svg></span>
</section>

<footer class="site-footer">
  <div class="newsletter">
    <h3>Stay Always In Touch</h3>
    <div class="field">Email Address<span class="btn">SUBSCRIBE</span></div>
  </div>
  <div class="footer-cols">
    <div class="col-about">
      <h4>ABOUT US</h4>
      <p>In 1996, our firm was founded and is comprised of 5 Partners and over 15 Associates and support staff fully engaged and focused on client service. The firm is fully automated and is run on the latest practice management software with efficient client focused delivery systems and improved turn around times.</p>
      <div class="footer-social"><i class="dot"></i><i class="dot"></i><i class="dot"></i><i class="dot"></i></div>
    </div>
    <div class="col-links">
      <h4>USEFUL LINKS</h4>
      <ul><li>About Us</li><li>Areas of Practice</li><li>Attorneys</li><li>Locations</li><li>Contact Us</li></ul>
    </div>
    <div class="col-services">
      <h4>OUR SERVICES</h4>
      <ul><li>Construction Law</li><li>Arbitration</li><li>Litigation</li></ul>
    </div>
    <div class="col-contact">
      <h4>GET IN TOUCH</h4>
      <p><svg width="9" height="12" viewBox="0 0 9 12"><path d="M4.5 0A4.5 4.5 0 0 0 0 4.5C0 8 4.5 12 4.5 12S9 8 9 4.5A4.5 4.5 0 0 0 4.5 0z" fill="#a9a9a9"/><circle cx="4.5" cy="4.5" r="1.6" fill="#2a2a2a"/></svg><span><strong>BYARUHANGA &amp; ODONGO ADVOCATES</strong><br>Plot 8, Kampala Road<br>2nd Floor, Nile House<br>P.O Box 4410<br>Kampala, Uganda</span></p>
      <p><svg width="9" height="9" viewBox="0 0 10 10"><path d="M2 1l2 2-1 1.5c.6 1.2 1.3 1.9 2.5 2.5L7 6l2 2-1.5 1.5C4.5 9 1 5.5.5 2.5z" fill="#a9a9a9"/></svg><span>0414 555 210<br>+256 (0) 700 123 456</span></p>
      <p><svg width="10" height="8" viewBox="0 0 10 8"><rect x=".5" y=".5" width="9" height="7" fill="none" stroke="#a9a9a9"/><path d="M.5.5l4.5 4 4.5-4" fill="none" stroke="#a9a9a9"/></svg><span>advocates@byodlaw.com</span></p>
    </div>
  </div>
  <div class="copyright">Byaruhanga &amp; Odongo Advocates © 2018. All Rights Reserved Terms of Use and Privacy Policy</div>
</footer>

</body>
</html>
```